Evergold Fernbark Inc

Industry/Entity Type

Forestry

Contact Information for Business Card

Company name: Evergold Fernbark INC, Contact Info: Rovelio Marquin, Phone # 912 555 0187, Addres: 284 Willowbend Creek Rd, Glenwood GA 30428, Email: evergoldfernbark@mailbrook.net

```html
<!DOCTYPE html>
<html lang="en">
<head>
<meta charset="utf-8">
<title>Evergold Fernbark INC — Business Card</title>
<link rel="stylesheet" href="https://fonts.googleapis.com/css2?family=Questrial&family=Tinos:wght@700&display=swap">
<style>
  :root {
    --stage: #d9d9d9;
    --card-dark: #1c1c1c;
    --card-light: #ffffff;
    --brand-green: #1e6b1e;
    --ink-grey: #4a4a4a;
    --ink-light: #f2f2f2;
  }
  html, body {
    margin: 0;
    width: 1200px;
    height: 800px;
    overflow: hidden;
    background: var(--stage);
  }
  .canvas {
    position: relative;
    width: 1200px;
    height: 800px;
  }
  .card {
    position: absolute;
    top: 250px;
    width: 525px;
    height: 300px;
    box-sizing: border-box;
    border-bottom: 3px solid var(--brand-green);
    box-shadow: 0 10px 24px rgba(0,0,0,0.18);
  }
  .card--back {
    left: 50px;
    background: var(--card-dark);
    display: flex;
    flex-direction: column;
    align-items: center;
    justify-content: center;
    text-align: center;
  }
  .card--front {
    left: 625px;
    background: var(--card-light);
    display: flex;
    align-items: center;
    justify-content: center;
  }
  .back__mark {
    width: 22px;
    height: 22px;
    background: var(--brand-green);
    margin-bottom: 10px;
  }
  .back__rule {
    width: 190px;
    height: 1px;
    background: var(--brand-green);
  }
  .back__name {
    font-family: "Tinos", serif;
    font-weight: 700;
    font-size: 22px;
    color: var(--brand-green);
    margin: 8px 0 10px;
    letter-spacing: 0.5px;
  }
  .back__details {
    font-family: "Questrial", sans-serif;
    font-size: 14.5px;
    line-height: 1.5;
    color: var(--ink-light);
    margin-bottom: 12px;
    white-space: nowrap;
  }
  .front__brand {
    display: flex;
    align-items: center;
    gap: 16px;
  }
  .front__square {
    width: 26px;
    height: 26px;
    background: var(--brand-green);
  }
  .front__name {
    font-family: "Questrial", sans-serif;
    font-size: 40px;
    line-height: 1.05;
    color: var(--ink-grey);
    letter-spacing: 0.3px;
    white-space: nowrap;
  }
</style>
</head>
<body>
  <main class="canvas">
    <section class="card card--back" aria-label="Business card back">
      <div class="back__mark"></div>
      <div class="back__rule"></div>
      <div class="back__name">Rovelio Marquin</div>
      <div class="back__details">
        284 Willowbend Creek Rd, Glenwood GA 30428<br>
        912 555 0187 | evergoldfernbark@mailbrook.net
      </div>
      <div class="back__rule"></div>
    </section>

    <section class="card card--front" aria-label="Business card front">
      <div class="front__brand">
        <div class="front__square"></div>
        <div class="front__name">Evergold<br>Fernbark INC</div>
      </div>
    </section>
  </main>
</body>
</html>
```